Maplecrest Apartments Downtown Northport

We are looking to redesign our entry way sign at Maplecrest Apartments, a low density residential apartment building, located in Downtown Northport, Alabama, U.S. Downtown Northport is a bustling boutique business district with a small town feel comprised of shops, restaurants, and a renowned arts community known for Varrow Arts Center and Festival which is one of the nation's top outdoor arts festivals. Maplecrest Apartments and its sign is the first thing you seen when you enter Downtown Northport. We are looking to redesign our sign, entry way and landscaping to compliment the building and character of the historic downtown.

Target Market(s)

Our apartment building is comprised of 20 apartments units with tenants who are primarily part of the local workforce, young professionals, or students at the Halverton College or other nearby institutions.

Requirements
Must have
• The name of the apartment building - Maplecrest
Phone number on the sign 205-555-0148

```html
<!DOCTYPE html>
<html lang="en">
<head>
<meta charset="utf-8">
<title>Maplecrest Apartments Sign</title>
<link rel="stylesheet" href="https://fonts.googleapis.com/css2?family=Rye&family=Montserrat:wght@700&display=swap">
<style>
  :root {
    --page: #ffffff;
    --wood-light: #dcc09a;
    --wood-mid: #c9a479;
    --wood-dark: #b88e62;
    --stone-deep: #3a220c;
    --stone-mid: #512f10;
    --stone-warm: #5e3a16;
    --sign-white: #ffffff;
    --ink-brown: #5a3513;
  }
  html, body {
    margin: 0;
    padding: 0;
    width: 1200px;
    height: 1200px;
    overflow: hidden;
    background: var(--page);
  }
  .canvas {
    position: relative;
    width: 1200px;
    height: 1200px;
  }
  .sign-frame {
    position: absolute;
    left: 122px;
    top: 330px;
    width: 958px;
    height: 542px;
    background: linear-gradient(90deg, var(--wood-light), var(--wood-mid) 45%, var(--wood-light) 70%, var(--wood-dark));
    box-shadow: 0 1px 3px rgba(0,0,0,0.35);
  }
  .sign-panel {
    position: absolute;
    left: 20px;
    top: 22px;
    width: 917px;
    height: 499px;
    overflow: hidden;
  }
  .stone-texture {
    position: absolute;
    inset: 0;
    background: radial-gradient(ellipse at 45% 35%, var(--stone-warm), var(--stone-mid) 55%, var(--stone-deep));
  }
  .sign-name {
    position: absolute;
    left: 0;
    top: 130px;
    width: 917px;
    height: 160px;
  }
  .sign-name text {
    font-family: "Rye", serif;
    font-size: 156px;
    fill: var(--sign-white);
  }
  .phone-band {
    position: absolute;
    left: 0;
    top: 328px;
    width: 917px;
    height: 96px;
    background: var(--sign-white);
    display: flex;
    align-items: center;
    justify-content: center;
    gap: 26px;
  }
  .phone-icon {
    width: 62px;
    height: 62px;
  }
  .phone-number {
    font-family: "Montserrat", sans-serif;
    font-weight: 700;
    font-size: 76px;
    color: var(--ink-brown);
    letter-spacing: 1px;
    line-height: 1;
  }
</style>
</head>
<body>
  <div class="canvas">
    <div class="sign-frame">
      <div class="sign-panel">
        <div class="stone-texture" role="img" aria-label="Dark brown fieldstone wall texture"></div>
        <svg class="sign-name" viewBox="0 0 917 160" aria-label="Maplecrest">
          <text x="458" y="138" text-anchor="middle" textLength="792" lengthAdjust="spacingAndGlyphs">MAPLECREST</text>
        </svg>
        <div class="phone-band">
          <svg class="phone-icon" viewBox="0 0 64 64" aria-hidden="true">
            <path d="M14 8c2-2 5-2 6 0l6 10c1 2 0 4-1 5l-4 3c2 6 8 12 14 14l3-4c1-1 3-2 5-1l10 6c2 1 2 4 0 6l-5 5c-3 3-9 3-16-1C22 46 14 38 9 28 5 21 5 15 8 12z" fill="var(--ink-brown)"/>
            <path d="M36 18a12 12 0 0 1 10 10M36 8a22 22 0 0 1 20 20" fill="none" stroke="var(--ink-brown)" stroke-width="4.5" stroke-linecap="round"/>
          </svg>
          <span class="phone-number">205-555-0148</span>
        </div>
      </div>
    </div>
  </div>
</body>
</html>
```